Realtor / Kitchen & Bath Designer / Curb Appeal Specialist Before & After Postcard

Realtor / Curb Appeal Specialist / Kitchen & Bath Designer / Interior Decorator / Real Estate Staging

I need an oversized postcard to send to luxury / waterfront homes and condominiums. I have a background photo and 3 sets of Before and After photos and a professional photo for my bio which I would like to be on the back with room for address labels and postage.

I offer a FREE (No obligation) in-home design / staging consultation for potential homeowners interesed in selling their home or condominium. I will place some of these cards in open houses, related businesses, some will be direct mailed, some will be handed out.

My goal with this marketing is to attract potential SELLERS who realize that they need my skills, ideas, experience for: Curb Appeal / Facade Enhancement / landscaping ... Kitchen & Bath Updating ... Decorating / Paint Colors ... Staging, etc ... in order to help SELL their properties FASTER and with HIGHER NET PROCEEDS on the real estate market ... and HOPEFULLY LISTING their property with me as their Listing Realtor.

I realize this is a bit complicated but I hopfully the photos will mostly convey the message ... with text as needed, more elegantly than I have worded this. Here are some POINTS that I am trying to make:

Curb Appeal, Landscaping, Updated Kitchens & Baths, Paint Colors, Lighting ... are more important than ever ... to sell upscale waterfront homes/condominiums in this competitive market ... design savvy BUYERS are looking for quality fixtures, features, and WOW factors.

Bio. Brennic Dwale is a Florida Realtor and licensed Interior Decorator, Kitchen & Bath Designer, and Curb Appeal Specialist with 25+ years experience in the residential design/remodeling industry.

Photos are: Professional photo (can be cropped and/or B/W with Bio on back) ... Photos are in order: 6 sets of Before - After, with addtional photo.

Target Market(s)

Home and Condo owners who are wanting to SELL their home and hopefully LIST with me as a REALTOR. I also pick up some design work.

Industry/Entity Type

Landscaping

Requirements
Must have
• Front: The entire front could be a faded - muted (half tone) photo of the kitchen (last photo) ... then 3 or 4 sets of smaller before & after pics with borders. The after photos could be slightly larger than the before pics which could be inset or superimposed/offset at the bottom. There should be a lead line at the top such as :

"Serious about selling your home or condominium?" and maybe at the bottom: "Today's design savvy BUYERS desire updated kitchens and baths, quality fixtures, design features, and attractive landscaping."

Back: My bio with photo. Room for hand written or address labels/postage. Perhaps the Before & After of the condo bathroom could also be on the back at the left /top with my photo/bio smaller at the left bottom.
Nice to have
• somehow make it seem classy and elegant ... not like a sales pitch
Should not have
• anything that looks or sounds tacky.

```html
<!DOCTYPE html>
<html lang="en">
<head>
<meta charset="utf-8">
<title>Before &amp; After Postcard – Brennic Dwale</title>
<link rel="stylesheet" href="https://fonts.googleapis.com/css2?family=Roboto+Condensed:ital,wght@0,300;0,400;0,700;1,400;1,700&family=Caveat:wght@400&display=swap">
<style>
  :root {
    --slate: #34495a;
    --slate-text: #3d4a57;
    --steel: #5f6b77;
    --mint: #7fcfae;
    --tan: #b39a62;
    --paper: #f4f2ec;
    --page: #ffffff;
    --rule: #d8d4ca;
  }
  * { box-sizing: border-box; margin: 0; padding: 0; }
  html, body { width: 1200px; height: 960px; overflow: hidden; background: var(--page); }
  body { position: relative; font-family: "Roboto Condensed", "Arial Narrow", sans-serif; color: var(--slate-text); }

  .card { position: absolute; width: 542px; height: 421px; background: var(--paper); overflow: hidden; }
  .card--back { left: 43px; top: 270px; }
  .card--front { left: 615px; top: 270px; }

  /* Front */
  .front-band { position: absolute; left: 0; top: 0; width: 100%; height: 33px; background: var(--slate); }
  .front-gallery { position: absolute; left: 0; top: 35px; width: 542px; height: 142px; }
  .tag-before { font: 700 8px "Roboto Condensed", sans-serif; fill: var(--slate); letter-spacing: .2px; }
  .tag-after { font: 400 17px "Caveat", cursive; fill: var(--tan); }
  .color-bar { position: absolute; display: flex; height: 7px; }
  .color-bar span { display: block; height: 100%; }
  .front-bar { left: 0; top: 180px; width: 542px; }

  .headline { position: absolute; left: 44px; top: 232px; font-weight: 300; font-size: 29px; line-height: 35px; color: var(--slate-text); letter-spacing: -.2px; }
  .headline .accent { color: var(--tan); }
  .lead { position: absolute; left: 44px; top: 318px; width: 318px; font-size: 13px; line-height: 17px; color: var(--slate-text); }
  .lead strong { font-weight: 700; }

  .portrait { position: absolute; background: linear-gradient(180deg, #d9c9a8 0%, #a58f6c 45%, #2c2f36 100%); }
  .front-portrait { left: 450px; top: 241px; width: 59px; height: 74px; }
  .agent { position: absolute; left: 450px; top: 326px; width: 70px; }
  .agent-name { font-size: 10px; color: var(--mint); }
  .agent-role { margin-top: 3px; font-style: italic; font-size: 6.5px; line-height: 8px; color: var(--slate-text); }
  .agent-phone { margin-top: 6px; font-weight: 700; font-size: 7.5px; color: var(--slate-text); }

  /* Back */
  .back-gallery { position: absolute; left: 0; top: 29px; width: 264px; height: 68px; }
  .back-intro { position: absolute; left: 29px; top: 118px; width: 236px; font-size: 10px; line-height: 11.6px; color: var(--slate-text); }
  .back-intro p + p { margin-top: 8px; }
  .services-title { position: absolute; left: 29px; top: 224px; font-weight: 700; font-size: 10px; line-height: 12px; color: var(--slate-text); }
  .services { position: absolute; left: 29px; top: 242px; list-style: none; font-size: 9px; line-height: 11px; color: var(--slate-text); }
  .services li { width: 82px; height: 18.5px; padding-top: 3px; white-space: nowrap; border-bottom: 1px solid var(--rule); }
  .services li:last-child { border-bottom: none; }
  .back-bar { left: 0; top: 325px; width: 264px; }
  .bio-box { position: absolute; left: 0; top: 342px; width: 197px; height: 50px; background: var(--mint); }
  .bio-text { position: absolute; left: 20px; top: 10px; width: 138px; font-style: italic; font-weight: 700; font-size: 5px; line-height: 6px; color: #ffffff; }
  .back-portrait { left: 162px; top: 4px; width: 33px; height: 42px; }
  .offer-box { position: absolute; left: 201px; top: 342px; width: 63px; height: 50px; background: var(--steel); padding: 5px 5px; font-size: 6.5px; line-height: 8px; color: #ffffff; }
  .offer-box strong { color: var(--mint); font-weight: 700; }
</style>
</head>
<body>

<section class="card card--back" aria-label="Postcard back">
  <svg class="back-gallery" viewBox="0 0 264 68" role="img" aria-label="Before and after photos of a house exterior and a remodelled kitchen">
    <rect x="0" y="0" width="130" height="68" fill="#9aa6a6"/>
    <polygon points="0,0 62,0 40,68 0,68" fill="#b7c2bf"/>
    <polygon points="66,0 130,0 130,68 44,68" fill="#6f6a5d"/>
    <line x1="64" y1="0" x2="42" y2="68" stroke="#ffffff" stroke-width="2"/>
    <rect x="133" y="0" width="131" height="68" fill="#c9c2b6"/>
    <polygon points="133,0 195,0 175,68 133,68" fill="#dcd8d0"/>
    <polygon points="199,0 264,0 264,68 179,68" fill="#7a5638"/>
    <line x1="197" y1="0" x2="177" y2="68" stroke="#ffffff" stroke-width="2"/>
    <line x1="131.5" y1="0" x2="131.5" y2="68" stroke="#ffffff" stroke-width="3"/>
  </svg>

  <div class="back-intro">
    <p>It is paramount that a buyer’s first impression of your home inspires a vision of their desired lifestyle.</p>
    <p>Leave design decisions to me and experience interiors with a difference. International research shows that staged homes sell faster, maximising price potential.<br>I have over 25 years experience in the residential design/remodeling industry.</p>
  </div>

  <h3 class="services-title">I offer experience in:</h3>
  <ul class="services">
    <li>Curb appeal</li>
    <li>Facade enhancement/ landscaping</li>
    <li>Kitchen and bathroom design</li>
    <li>Color consultancy</li>
  </ul>

  <div class="color-bar back-bar" aria-hidden="true">
    <span style="width:38px;background:var(--slate)"></span>
    <span style="width:98px;background:var(--steel)"></span>
    <span style="width:17px;background:var(--mint)"></span>
    <span style="width:38px;background:var(--tan)"></span>
    <span style="width:73px;background:var(--slate)"></span>
  </div>

  <div class="bio-box">
    <p class="bio-text">Brennic Dwale is a Florida Realtor and licensed interior decorator, kitchen &amp; bath designer, and curb appeal specialist with 25+ years experience in the residential design/remodeling industry.</p>
    <div class="portrait back-portrait" role="img" aria-label="Portrait of Brennic Dwale"></div>
  </div>
  <div class="offer-box">I offer a <strong>FREE</strong> (no obligation) in-home design / staging consultation</div>
</section>

<section class="card card--front" aria-label="Postcard front">
  <div class="front-band" aria-hidden="true"></div>

  <svg class="front-gallery" viewBox="0 0 542 142" role="img" aria-label="Before and after photos of a house facade and a fireplace makeover">
    <rect x="0" y="0" width="268" height="142" fill="#8d9e86"/>
    <polygon points="0,0 137,0 77,142 0,142" fill="#9fb8a6"/>
    <polygon points="141,0 268,0 268,142 81,142" fill="#a5aaa6"/>
    <line x1="139" y1="0" x2="79" y2="142" stroke="#ffffff" stroke-width="2.5"/>
    <rect x="272" y="0" width="270" height="142" fill="#b59a74"/>
    <polygon points="272,0 435,0 335,142 272,142" fill="#b8a283"/>
    <polygon points="439,0 542,0 542,142 339,142" fill="#3c3836"/>
    <rect x="510" y="0" width="32" height="142" fill="#c9c2b6"/>
    <line x1="437" y1="0" x2="337" y2="142" stroke="#ffffff" stroke-width="2.5"/>
    <line x1="270" y1="0" x2="270" y2="142" stroke="#ffffff" stroke-width="4"/>
    <text class="tag-before" x="7" y="15">BEFORE</text>
    <text class="tag-after" x="224" y="134">After</text>
    <text class="tag-before" x="279" y="15">BEFORE</text>
    <text class="tag-after" x="366" y="134">After</text>
  </svg>

  <div class="color-bar front-bar" aria-hidden="true">
    <span style="width:80px;background:var(--slate)"></span>
    <span style="width:200px;background:var(--steel)"></span>
    <span style="width:34px;background:var(--mint)"></span>
    <span style="width:78px;background:var(--tan)"></span>
    <span style="width:150px;background:var(--slate)"></span>
  </div>

  <h1 class="headline">Serious <span class="accent">about selling</span> your<br>home or condominium?</h1>
  <p class="lead">Today’s design savvy <strong>BUYERS</strong> desire updated<br>kitchens and baths, quality fixtures, design features,<br>and attractive landscaping.</p>

  <div class="portrait front-portrait" role="img" aria-label="Portrait of Brennic Dwale"></div>
  <div class="agent">
    <p class="agent-name">Brennic Dwale</p>
    <p class="agent-role">Florida Realtor and Licensed Interior Decorator</p>
    <p class="agent-phone">Phone number</p>
  </div>
</section>

</body>
</html>
```